2 sets of Business cards, stationary/envelopes, stationary template(MS Word), door hang tag
KRV Building Works, LLC (Design A) and Steadfield Estate Holdings, LLC (Design B)
2 sets of Business cards, stationary/envelopes, stationary template(MS Word), door hang tag - Real Estate
Creative Brief
Simple
Darrel K. Winton
Managing Member
5120 Larkspur Lane, Suite B Brookhaven, KS 66102
Don't know yet, but need space for it
dwinton@krvbuildworks.com
www.krvbuildworks.com (Design A) and www.steadfieldleasing.com (Design B)
We are a family owned business with 90+ years in the construction and real estate sector and would like to present our company as a quality, professional organization with a sleek modern set of stationary. Stationary design A: Company name: KRV Building Works, LLC Optional Tagline: Working from experience, not for it! Color Mode: RGB color Grey :R=149 G=149 B=149 White: R=255 G=255 B=255 Black : R=0 G=0 B=0 Blue : R=0 G=97 B=240 dwinton@krvbuildworks.com (Design A) For: KRV Building Works, LLC Stationary design B: Company name: Steadfield Estate Holdings, LLC Optional Tagline: Steadfield Precision, Steadfield Dedication Color Mode: RGB color Grey :R=149 G=149 B=149 White: R=255 G=255 B=255 Black : R=0 G=0 B=0 Red : R=209 G=0 B=0 dwinton@steadfieldleasing.com (Design B) For: Steadfield Estate Holdings, LLC Phone, email, and name will change for the additional members of the company. We also want an electronic email signature, and digital stationary template (MS word). Stationary and envelopes should tie in the theme of the business cards for a uniform look. Also looking for a Header only version of the stationary, as well as a full page version (header and footer used for design).
Logo used in a creative way.
darrelkwinton darrelkwinton
Sorry, been out of the office. Waiting for partners to look at everything before making comments. We should be leaving comments and making recommendations in the next day or two for all of the designs we want to see refined. Thanks, Darrel

```html
<!DOCTYPE html>
<html lang="en">
<head>
<meta charset="utf-8">
<title>KRV Building Works – Business Cards</title>
<link rel="stylesheet" href="https://fonts.googleapis.com/css2?family=Questrial&display=swap">
<style>
  :root {
    --backdrop: #e4e4e6;
    --card-white: #ffffff;
    --card-black: #0b0b0d;
    --brand-blue: #0061f0;
    --brand-grey: #959595;
    --ink: #3a3a3a;
    --ink-soft: #6a6a6a;
  }
  * { box-sizing: border-box; margin: 0; padding: 0; }
  html, body {
    width: 1200px; height: 901px; overflow: hidden;
    background: var(--backdrop);
    font-family: "Questrial", "Century Gothic", sans-serif;
  }
  .stage { position: relative; width: 1200px; height: 901px; }

  .card {
    position: absolute; width: 630px; height: 360px;
    box-shadow: 0 6px 18px rgba(0,0,0,.18);
    overflow: hidden;
  }

  /* Back of card */
  .card--back { left: 60px; top: 60px; background: var(--card-black); }
  .card--back .wordmark {
    position: absolute; left: 50%; top: 50%; transform: translate(-50%, -50%);
    display: flex; align-items: center; gap: 14px;
  }
  .card--back .wordmark__name { color: var(--card-white); white-space: nowrap; }

  /* Front of card */
  .card--front { left: 510px; top: 480px; background: var(--card-white); }
  .card--front .wordmark {
    position: absolute; left: 48px; top: 122px;
    display: flex; align-items: center; gap: 14px;
  }
  .card--front .wordmark__name { color: var(--brand-blue); }

  .wordmark__square {
    width: 32px; height: 32px; background: var(--brand-grey); flex: none;
  }
  .wordmark__name {
    font-size: 22px; line-height: 1.15; letter-spacing: 1px;
    text-transform: uppercase;
  }

  .contact {
    position: absolute; left: 360px; top: 40px; width: 250px;
    color: var(--ink); font-size: 12px; line-height: 1.45;
  }
  .contact__name { color: var(--brand-blue); font-size: 18px; line-height: 1.2; }
  .contact__title { color: var(--ink-soft); font-size: 12px; margin-bottom: 14px; }
  .contact__address { margin-bottom: 12px; }
  .contact__list { list-style: none; }
  .contact__item { display: flex; align-items: center; gap: 8px; white-space: nowrap; }
  .contact__icon { width: 11px; height: 11px; flex: none; }

  .footer-band {
    position: absolute; left: 0; bottom: 0; width: 100%; height: 14px;
    display: flex;
  }
  .footer-band__grey { width: 40%; background: var(--brand-grey); }
  .footer-band__blue { width: 60%; background: var(--brand-blue); }
</style>
</head>
<body>
<main class="stage">

  <section class="card card--back" aria-label="Business card back">
    <div class="wordmark">
      <span class="wordmark__square"></span>
      <span class="wordmark__name">KRV Building Works</span>
    </div>
  </section>

  <section class="card card--front" aria-label="Business card front">
    <div class="wordmark">
      <span class="wordmark__square"></span>
      <span class="wordmark__name">KRV<br>Building Works</span>
    </div>

    <div class="contact">
      <p class="contact__name">Darrel K. Winton</p>
      <p class="contact__title">Managing Member</p>
      <p class="contact__address">5120 Larkspur Lane, Suite B<br>Brookhaven, KS 66102</p>
      <ul class="contact__list">
        <li class="contact__item">
          <svg class="contact__icon" viewBox="0 0 12 12"><rect x="3" y="1" width="6" height="10" rx="1" fill="var(--brand-blue)"/></svg>
          (555) 010-0100
        </li>
        <li class="contact__item">
          <svg class="contact__icon" viewBox="0 0 12 12"><path d="M2 3h8v6H2z" fill="var(--brand-blue)"/><rect x="4" y="1" width="4" height="2" fill="var(--brand-blue)"/></svg>
          (555) 010-0111
        </li>
        <li class="contact__item">
          <svg class="contact__icon" viewBox="0 0 12 12"><path d="M3 1l2 3-1 1.5c.7 1.3 1.6 2.2 2.9 2.9L8.4 7l3 2-1 2C6 11 1 6 1 2z" fill="var(--brand-blue)"/></svg>
          (555) 014-2286
        </li>
        <li class="contact__item">
          <svg class="contact__icon" viewBox="0 0 12 12"><rect x="1" y="3" width="10" height="7" fill="var(--brand-blue)"/><rect x="3" y="1" width="6" height="3" fill="var(--brand-blue)"/></svg>
          (555) 017-3390
        </li>
        <li class="contact__item">
          <svg class="contact__icon" viewBox="0 0 12 12"><rect x="1" y="2.5" width="10" height="7" fill="var(--brand-blue)"/><path d="M1 3l5 4 5-4" stroke="#fff" fill="none"/></svg>
          dwinton@krvbuildworks.com
        </li>
        <li class="contact__item">
          <svg class="contact__icon" viewBox="0 0 12 12"><circle cx="6" cy="6" r="5" fill="var(--brand-blue)"/></svg>
          www.krvbuildworks.com
        </li>
      </ul>
    </div>

    <div class="footer-band">
      <span class="footer-band__grey"></span>
      <span class="footer-band__blue"></span>
    </div>
  </section>

</main>
</body>
</html>
```